Web Design (Coded) and Project - Finance Company

Corvale Lending Group is a mortgage broker company based in Sydney Australia and provides lending solutions for individuals and businesses.

Our target market is anyone with the financial means to get a loan.

I am looking for a website design in this contest. The site needs to be able to be viewed on a portable device such as Tabra, Fonix, etc.

I have the logo design and files which need to be used. I also have the NLBC logo which will need to be in the footer of each page.

The website needs to represent a big finance company with integrity and knowledge.

The website will need to be uploaded to Hostwillow.example.au as they are the hosting provider. I will also need the ability to make changes to the text and pictures in the future and upload the revisions. I need the website ready to go and ready to be uploaded onto Host Willow.

The website will consist of 6 pages in total There are 4 main pages that will be viewed and then 2 with Privacy and Internal Dispute Resolution which are only accessed through links. These will be as follows:

Home
I would prefer to have a fresh bright and professional looking home page given that most mortgage broker websites look the same with the menu buttons at the top.

Services
Details the loan types that we handle and some text for each one.

About Us
I have the text for this.

Contact Us
Form to have the following inputs:
• Surname
• First Name
• Suburb
• State
• Phone number
• Mobile number
• Email address
• Preferred contact
o Phone
o Mobile
o Email
• Reason for Enquiry
o First home buyer
o Refinance
o Investment Property
o Commercial lending
o Personal loan
o Other
• Comments

Privacy
This page will only be accessed from a link at the bottom of each page. I have the wording that I will provide.

Dispute Resolution Policy
This page will only be accessed from a link on the Contact Us page. I have the wording that I will provide.
Updates

The designs that are coming through so far are generally looking the same generic website layout. I am looking for the home page to be something different with more of a wow factor and something different to the standard page link menu accross the top of the screen. The content should be fairly minimal given that I am a new business there will be limited text for each page. I am happy to increase the budget if required as I appreciate there will be more work involved.

Reason: I am extending the deadline as the design so far are good but fairly generic and template style home pages. For the home page I am looking for something a little more striking with a visual impact.

I have increased the payment by $200 to encourage more designs. Designs need to be relevant to the business, the number of pages and content. Several designs have come through looking good but just look like a standard template with my logo added, but the content does not match the business.

The brief stated that I am looking for the home page to be something different with more of a wow factor and something different to the standard page link menu accross the top of the screen. All of the designs have come through with the navigation bar along the top and a generic layout. I have attached a couple of idea's. Obviously these do not relate to the finance and mortgage industry but you can see the sort of style that gives the site a wow factor. The other pages can be more generic, but the first page is the attention grabber. You can also see the Fonix view that I am after. These are just templates from Host Willow that I could use to build the site, I just don't have the time or creative flair. Please submit more designs. Thanks for your work to date, Rob.

Hi. Could you please submit designs based on brief and the two screen shots attached. Mobile device view should work as per screen shots. Thanks, Rob

Reason: Still looking for designs to meet the brief provided.

Industry/Entity Type

Financial

Requirements
Must have
• Colour palette to be as supplied. I will post this shortly.
Should not have
• No cheesy smiley faces
No handshaking
No money pictures
No pictures of stones
No picture of people in an office looking at things
No lime green or purple in colour
Would prefer not to have a picture of the Quayline Span or Tidewater Hall

```html
<!DOCTYPE html>
<html lang="en">
<head>
<meta charset="utf-8">
<title>Corvale Lending Group</title>
<link href="https://fonts.googleapis.com/css2?family=Open+Sans:ital,wght@0,400;0,600;0,700;1,400;1,700&family=Oswald:wght@500&display=swap" rel="stylesheet">
<style>
:root{
  --teal-dark:#0b3f57;
  --teal:#14617f;
  --teal-bright:#1c7da3;
  --blue-btn:#2f8fe0;
  --ink:#2b2b2b;
  --ink-soft:#4a4a4a;
  --text:#555a5e;
  --panel:#2c2c2c;
  --page:#f1f3f4;
  --white:#ffffff;
  --card-border:#d8dadc;
  --footer:#e3e4e5;
  --footer-bar:#d4d5d6;
  --orange:#f07f1e;
  --link-blue:#1a78b8;
  --nav-active:#2fa3e6;
  --badge:#1f5fa5;
}
*{margin:0;padding:0;box-sizing:border-box}
html,body{width:840px;height:1200px;overflow:hidden}
body{background:var(--page);font-family:"Open Sans",sans-serif;color:var(--text);position:relative}
.abs{position:absolute}

.top-bar{left:0;top:0;width:840px;height:28px;background:linear-gradient(var(--teal),var(--teal-dark));border-bottom:1px solid #08324a}
.top-links{right:26px;top:7px;font-size:10.5px;color:var(--white);display:flex;gap:12px}
.top-links span.sep{opacity:.8}

.brand{left:34px;top:54px;display:flex;align-items:center;gap:10px}
.brand-mark{width:52px;height:52px;border-radius:50%;background:var(--teal-bright)}
.brand-name{font-weight:700;font-size:15px;line-height:16px;color:#2f3a44;letter-spacing:.5px;text-transform:uppercase}

.call{right:30px;top:89px;font-size:12px;color:var(--ink)}
.call b{font-style:italic;font-weight:700}
.call .phone{color:var(--orange);font-style:italic;margin-left:4px}

.side-nav{left:27px;top:130px;width:148px;height:340px}
.side-nav ul{list-style:none;position:absolute;left:10px;top:20px;width:122px}
.side-nav li{font-size:10.5px;color:#e5e5e5;padding:6px 0 6px 7px;border-bottom:1px dashed #6a6a6a;text-transform:uppercase}
.side-nav li.active{color:var(--nav-active)}
.side-nav li:last-child{border-bottom:none}
.follow{left:0;width:148px;top:246px;text-align:center;font-size:10.5px;color:#d9d9d9}
.social-btn{left:29px;top:268px;width:88px;height:30px;background:#3b5b98;border:1px solid #8aa0c8;color:var(--white);font-size:11px;font-weight:600;text-align:center;line-height:28px}

.hero{left:183px;top:129px;width:635px;height:235px;background:linear-gradient(120deg,#3d5a23 0%,#8aa64a 35%,#c99a78 55%,#a7c15a 80%,#e6d33a 100%)}
.hero-dots{left:452px;top:364px;width:72px;height:14px;background:#2e3b44;border-radius:0 0 6px 6px}
.strip{left:183px;top:364px;width:635px;height:106px;background:var(--white);border-bottom:4px solid #dcdddd}
.strip-label{font-size:10px;color:var(--ink)}
.carousel{height:57px;background:var(--white);border:1px solid #cfd3d6;border-left:20px solid var(--teal);border-right:20px solid var(--teal)}
.carousel .arrow-l,.carousel .arrow-r{position:absolute;top:20px}
.carousel .arrow-l{left:-14px}
.carousel .arrow-r{right:-14px}
.testimonial-text{font-size:9.5px;color:var(--ink-soft);line-height:13px;position:absolute;left:13px;top:15px;width:210px}
.lenders{position:absolute;left:0;right:0;top:0;bottom:0;display:flex;align-items:center;justify-content:space-around;font-weight:600;font-size:15px;color:var(--teal)}

.card{top:504px;width:208px;height:281px;background:var(--white);border:1px solid var(--card-border);border-radius:3px}
.card-head{height:28px;background:linear-gradient(#333a40,#22282c);color:var(--white);font-family:"Oswald",sans-serif;font-size:13px;text-align:center;line-height:28px;border-radius:3px 3px 0 0;text-transform:uppercase}
.card-photo{position:absolute;left:7px;top:43px;width:193px;height:112px}
.card-text{position:absolute;left:7px;top:167px;width:193px;font-size:9.5px;line-height:13px;text-align:justify}
.btn-dark{position:absolute;left:57px;top:243px;width:82px;height:26px;background:#1f2a31;color:var(--white);font-size:9.5px;text-align:center;line-height:26px;border-radius:2px}

.section-head{font-family:"Oswald",sans-serif;font-size:15px;color:var(--ink);text-transform:uppercase}
.body-copy{font-size:9.5px;line-height:15px;color:var(--ink-soft)}
.news-meta{color:var(--link-blue);font-style:italic}
.btn-blue{width:80px;height:21px;background:linear-gradient(#4aa6ee,var(--blue-btn));color:var(--white);font-size:9.5px;text-align:center;line-height:21px}

.footer{left:0;top:1006px;width:840px;height:155px;background:var(--footer)}
.back-top{left:668px;top:990px;width:82px;height:17px;background:var(--footer);border-radius:8px 8px 0 0;font-size:9.5px;color:var(--ink);text-align:center;line-height:18px}
.link-col{top:1022px}
.link-col h4{font-size:11px;font-weight:700;color:var(--ink-soft);margin-bottom:9px;text-transform:uppercase}
.link-col li{list-style:none;font-size:11px;color:#6a6d70;line-height:17px}
.footer-note{left:640px;top:1036px;width:165px;font-size:9.5px;line-height:13px;color:var(--ink-soft)}
.badge{left:659px;top:1090px;width:112px;height:41px;background:var(--white);border:2px solid var(--badge)}
.badge-fill{position:absolute;left:4px;top:4px;right:4px;bottom:4px;background:linear-gradient(90deg,#2f7fc0,#4bb85a)}
.legal{left:0;top:1161px;width:840px;height:39px;background:var(--footer-bar);font-size:10px;color:var(--ink);display:flex;justify-content:center;align-items:center;gap:14px}
</style>
</head>
<body>

<header>
  <div class="abs top-bar"></div>
  <nav class="abs top-links"><span>Contact us</span><span class="sep">|</span><span>Quicklink1</span><span class="sep">|</span><span>Quicklink2</span><span class="sep">|</span><span>Quicklink3</span></nav>

  <div class="abs brand">
    <div class="brand-mark"></div>
    <div class="brand-name">Corvale<br>Lending<br>Group</div>
  </div>
  <div class="abs call"><b>Speak with us today :</b><span class="phone">(000) 555 - 210 - 318</span></div>
</header>

<aside class="abs side-nav">
  <svg class="abs" style="left:0;top:0" width="148" height="340" viewBox="0 0 148 340">
    <path d="M0 0H148V300L74 340L0 300Z" fill="#2c2c2c"/>
    <path d="M5 5H143V296L74 333L5 296Z" fill="none" stroke="#6a6a6a" stroke-dasharray="3 2"/>
  </svg>
  <ul>
    <li class="active">Home</li>
    <li>About Us</li>
    <li>Our Services</li>
    <li>Contact Us</li>
  </ul>
  <div class="abs follow">Follow us on :</div>
  <div class="abs social-btn">Gatherly</div>
</aside>

<section class="hero-area">
  <div class="abs hero" role="img" aria-label="Father hugging his young daughter outdoors among green foliage"></div>
  <div class="abs hero-dots">
    <svg width="72" height="14"><g fill="#5d8fb0"><circle cx="20" cy="7" r="2.5"/><circle cx="30" cy="7" r="2.5" fill="#3aa3e0"/><circle cx="40" cy="7" r="2.5"/><circle cx="50" cy="7" r="2.5"/><circle cx="60" cy="7" r="2.5"/></g></svg>
  </div>
  <div class="abs strip"></div>

  <div class="abs strip-label" style="left:226px;top:378px">Client Testimonials</div>
  <div class="abs carousel" style="left:205px;top:393px;width:277px">
    <svg class="arrow-l" width="8" height="14"><path d="M8 0V14L0 7Z" fill="#0b2c3d"/></svg>
    <p class="testimonial-text">Nunc vulputate tristique molestie. Aliquam eu sem condimentum tristique nec</p>
    <svg class="arrow-r" width="8" height="14"><path d="M0 0V14L8 7Z" fill="#0b2c3d"/></svg>
  </div>

  <div class="abs strip-label" style="left:543px;top:377px">Panel Lenders</div>
  <div class="abs carousel" style="left:522px;top:393px;width:277px">
    <svg class="arrow-l" width="8" height="14"><path d="M8 0V14L0 7Z" fill="#0b2c3d"/></svg>
    <div class="lenders"><span>Veltora</span><span>Lumenfold</span><span>Plainmark</span></div>
    <svg class="arrow-r" width="8" height="14"><path d="M0 0V14L8 7Z" fill="#0b2c3d"/></svg>
  </div>
</section>

<section class="features">
  <article class="abs card" style="left:78px">
    <div class="card-head">Lorem Ipsum Dolor Sit</div>
    <div class="card-photo" role="img" aria-label="Smiling young woman holding a phone" style="background:linear-gradient(135deg,#f5f1ea,#e8c9a8 45%,#f3e7d2)"></div>
    <p class="card-text">Financial Services are committed to best practice financial management delivered professionally and within agreed time-frames. We endeavour to build strategic partnerships</p>
    <div class="btn-dark">READ MORE</div>
  </article>
  <article class="abs card" style="left:317px">
    <div class="card-head">Lorem Ipsum Dolor Sit</div>
    <div class="card-photo" role="img" aria-label="Couple talking together at home" style="background:linear-gradient(120deg,#d9d4c6,#b08a6c 40%,#e7c9ae 70%,#f1e6da)"></div>
    <p class="card-text">Financial Services are committed to best practice financial management delivered professionally and within agreed time-frames. We endeavour to build strategic partnerships</p>
    <div class="btn-dark">READ MORE</div>
  </article>
  <article class="abs card" style="left:555px">
    <div class="card-head">Lorem Ipsum Dolor Sit</div>
    <div class="card-photo" role="img" aria-label="Calculator and pen resting on a printed financial chart" style="background:linear-gradient(135deg,#3f6fa8,#aebfd4 35%,#e4e8ee 70%,#c9d2dc)"></div>
    <p class="card-text">Financial Services are committed to best practice financial management delivered professionally and within agreed time-frames. We endeavour to build strategic partnerships</p>
    <div class="btn-dark">READ MORE</div>
  </article>
</section>

<section class="about">
  <h2 class="abs section-head" style="left:81px;top:805px">About Us</h2>
  <p class="abs body-copy" style="left:80px;top:843px;width:328px;text-align:justify">Financial Services are committed to best practice financial management delivered professionally and within agreed timeframes. We endeavour to build strategic partnerships with our customers, the Faculties and the Departments, to provide both leadership and practical support for the University's financial operations and long term economic sustainability.</p>
  <div class="abs btn-blue" style="left:78px;top:947px">READ MORE</div>
</section>

<section class="news">
  <h2 class="abs section-head" style="left:436px;top:805px">Latest News</h2>
  <p class="abs body-copy" style="left:434px;top:842px;width:330px;line-height:13.5px">Nunc vulputate tristique molestie. Aliquam sed turpis eu sem condimentum tristique nec sed mauris. &nbsp;<span class="news-meta">posted by : lorem ipsum at 26-05-12</span></p>
  <p class="abs body-copy" style="left:434px;top:884px;width:330px;line-height:13.5px">Nunc vulputate tristique molestie. Aliquam sed turpis eu sem condimentum tristique nec sed mauris. &nbsp;<span class="news-meta">posted by : lorem ipsum at 26-05-12</span></p>
  <div class="abs btn-blue" style="left:434px;top:945px">READ MORE</div>
</section>

<footer>
  <div class="abs footer"></div>
  <div class="abs back-top">BACK TO TOP</div>

  <div class="abs link-col" style="left:56px"><h4>Link Heading 1</h4><ul><li>Bottom Quick Links</li><li>Bottom Quick Links</li><li>Bottom Quick Links</li><li>Bottom Quick Links</li><li>Bottom Quick Links</li><li>Bottom Quick Links</li></ul></div>
  <div class="abs link-col" style="left:190px"><h4>Link Heading 2</h4><ul><li>Bottom Quick Links</li><li>Bottom Quick Links</li><li>Bottom Quick Links</li><li>Bottom Quick Links</li><li>Bottom Quick Links</li><li>Bottom Quick Links</li></ul></div>
  <div class="abs link-col" style="left:339px"><h4>Link Heading 3</h4><ul><li>Bottom Quick Links</li><li>Bottom Quick Links</li><li>Bottom Quick Links</li><li>Bottom Quick Links</li><li>Bottom Quick Links</li><li>Bottom Quick Links</li></ul></div>
  <div class="abs link-col" style="left:474px"><h4>Link Heading 4</h4><ul><li>Bottom Quick Links</li><li>Bottom Quick Links</li><li>Bottom Quick Links</li><li>Bottom Quick Links</li><li>Bottom Quick Links</li><li>Bottom Quick Links</li></ul></div>

  <p class="abs footer-note">Nunc vulputate tristique molestie. Aliquam sed turpis eu sem condim entum tristique nec sed mauris.</p>
  <div class="abs badge" role="img" aria-label="Approved broker accreditation badge"><div class="badge-fill"></div></div>

  <div class="abs legal"><span>All Rights Reserved</span><span>|</span><span>Copyright 2012</span><span>|</span><span>Privacy Policy</span></div>
</footer>

</body>
</html>
```